Brochure 2 fold and Trifold

We need 2 types of brochure (2 fold and Trifold) design for our Brand "VELOURA BRIGHT" Logo (La douceur de Sorène) is in rose gold color
Target Market(s)
Women ages 17 and up
Industry/Entity Type
Supplement
Font styles to use
Serif
Script
Requirements
Must have
- Rose gold color tone make it look premium, minimalist look

```html
<!DOCTYPE html>
<html lang="en">
<head>
<meta charset="utf-8">
<title>Veloura Bright Brochures</title>
<link rel="stylesheet" href="https://fonts.googleapis.com/css2?family=Cormorant+Garamond:wght@400;600;700&family=Great+Vibes&family=Montserrat:wght@300;400;600&display=swap">
<style>
  :root {
    --backdrop: #cbc6c5;
    --rose: #efcbbd;
    --rose-deep: #e6b8a6;
    --rose-ink: #c98f7a;
    --band: #d9b3a4;
    --paper: #ffffff;
    --ink: #5b5b5b;
    --ink-soft: #9a9a9a;
    --bar-red: #c8433f;
    --bar-blue: #3f73b8;
    --bar-orange: #e07a3c;
    --white: #ffffff;
  }
  * { box-sizing: border-box; margin: 0; padding: 0; }
  html, body { width: 1200px; height: 979px; overflow: hidden; }
  body {
    background: var(--backdrop);
    font-family: "Montserrat", sans-serif;
    position: relative;
  }

  /* ---------- Bifold brochure ---------- */
  .bifold {
    position: absolute;
    left: 560px; top: 70px;
    display: flex;
    box-shadow: 0 10px 30px rgba(0,0,0,0.12);
  }
  .panel { width: 300px; height: 560px; position: relative; }

  .cover { background: var(--rose); color: var(--white); }
  .cover-frame {
    position: absolute; inset: 18px;
    border: 1px solid rgba(255,255,255,0.85);
  }
  .brand-mark {
    position: absolute; top: 70px; left: 0; right: 0;
    text-align: center;
    font-family: "Cormorant Garamond", serif;
    font-size: 17px; font-weight: 400; letter-spacing: 2px;
    color: var(--white);
  }
  .product-title {
    position: absolute; top: 250px; left: 40px; right: 30px;
    font-family: "Cormorant Garamond", serif;
    font-size: 34px; font-weight: 700; letter-spacing: 1.5px; line-height: 1.05;
    color: var(--white);
  }
  .product-tagline {
    position: absolute; top: 330px; left: 40px; right: 40px;
    font-size: 9px; font-weight: 300; letter-spacing: 1px;
    color: var(--white);
  }
  .floral-art {
    position: absolute; right: 18px; bottom: 18px;
    width: 170px; height: 150px;
    background: linear-gradient(135deg, rgba(255,255,255,0) 10%, rgba(255,255,255,0.55) 100%);
  }

  .inside { background: var(--paper); padding: 34px 30px; color: var(--ink); }
  .findings-title {
    font-family: "Cormorant Garamond", serif;
    font-size: 22px; font-weight: 700; letter-spacing: 2px;
    color: var(--rose-ink);
    margin-bottom: 16px;
  }
  .chart { display: block; margin-bottom: 10px; }
  .body-copy { font-size: 9.5px; line-height: 1.55; margin-bottom: 8px; }
  .source-note { font-size: 8px; color: var(--ink-soft); margin-bottom: 18px; }
  .legend { display: flex; gap: 14px; font-size: 8px; margin-bottom: 8px; }
  .legend-swatch { display: inline-block; width: 8px; height: 8px; margin-right: 4px; vertical-align: middle; }

  /* ---------- Trifold brochure ---------- */
  .trifold {
    position: absolute;
    left: 40px; top: 470px;
    display: flex;
    box-shadow: 0 10px 30px rgba(0,0,0,0.12);
  }
  .tri-panel {
    width: 165px; height: 400px;
    background: var(--rose);
    color: var(--white);
    position: relative;
    padding: 28px 16px;
    border-right: 1px solid rgba(255,255,255,0.35);
  }
  .tri-panel:last-child { border-right: none; }
  .tri-heading {
    font-family: "Cormorant Garamond", serif;
    font-size: 15px; font-weight: 600; letter-spacing: 1px;
    margin-bottom: 8px;
  }
  .tri-band {
    background: var(--band);
    font-size: 8px; font-weight: 600; letter-spacing: 1.5px;
    text-transform: uppercase;
    padding: 5px 8px;
    margin: 14px 0 6px;
  }
  .tri-list { list-style: none; font-size: 8.5px; line-height: 2; font-weight: 300; }
  .tri-list li { border-bottom: 1px solid rgba(255,255,255,0.45); }
  .tri-copy { font-size: 8.5px; line-height: 1.6; font-weight: 300; margin-bottom: 6px; }
  .tri-step { display: flex; gap: 8px; font-size: 8.5px; line-height: 1.5; font-weight: 300; margin-bottom: 8px; }
  .tri-step-num {
    flex: none; width: 16px; height: 16px; border-radius: 50%;
    border: 1px solid var(--white);
    font-size: 8px; text-align: center; line-height: 14px;
  }

  .tri-cover { text-align: center; }
  .script-name {
    margin-top: 80px;
    font-family: "Great Vibes", cursive;
    font-size: 30px; font-weight: 400; line-height: 1.1;
    color: var(--white);
  }
  .cover-rule {
    width: 60px; height: 1px; background: var(--white);
    margin: 16px auto;
  }
  .tri-brand {
    font-family: "Cormorant Garamond", serif;
    font-size: 13px; font-weight: 600; letter-spacing: 2.5px;
  }
  .tri-cover-note {
    position: absolute; left: 16px; right: 16px; bottom: 28px;
    font-size: 7.5px; font-weight: 300; letter-spacing: 1px;
  }
</style>
</head>
<body>

  <section class="trifold" aria-label="Trifold brochure, outside">
    <div class="tri-panel">
      <h3 class="tri-heading">Ingredients</h3>
      <p class="tri-copy">A gentle blend chosen for daily radiance.</p>
      <div class="tri-band">Key actives</div>
      <ul class="tri-list">
        <li>Glutathione 250 mg</li>
        <li>Vitamin C 100 mg</li>
        <li>Marine collagen</li>
        <li>Hyaluronic acid</li>
      </ul>
      <div class="tri-band">Botanicals</div>
      <ul class="tri-list">
        <li>Rose hip extract</li>
        <li>Grape seed extract</li>
        <li>Pomegranate extract</li>
      </ul>
    </div>
    <div class="tri-panel">
      <h3 class="tri-heading">How to use</h3>
      <div class="tri-step"><span class="tri-step-num">1</span><span>Take two capsules daily with water.</span></div>
      <div class="tri-step"><span class="tri-step-num">2</span><span>Best taken after breakfast.</span></div>
      <div class="tri-step"><span class="tri-step-num">3</span><span>Use for eight weeks for visible results.</span></div>
      <div class="tri-band">Benefits</div>
      <ul class="tri-list">
        <li>Brighter skin tone</li>
        <li>Even complexion</li>
        <li>Soft, hydrated skin</li>
        <li>Antioxidant support</li>
      </ul>
    </div>
    <div class="tri-panel tri-cover">
      <p class="script-name">La douceur de Sorène</p>
      <div class="cover-rule"></div>
      <p class="tri-brand">VELOURA BRIGHT</p>
      <p class="tri-cover-note">60 capsules · dietary supplement</p>
    </div>
  </section>

  <section class="bifold" aria-label="Bifold brochure">
    <article class="panel cover">
      <div class="cover-frame"></div>
      <p class="brand-mark">La douceur de Sorène</p>
      <h1 class="product-title">VELOURA BRIGHT</h1>
      <p class="product-tagline">Daily radiance supplement for luminous skin</p>
      <div class="floral-art" role="img" aria-label="White line-drawn leaves and flowers"></div>
    </article>

    <article class="panel inside">
      <h2 class="findings-title">CLINICAL FINDINGS</h2>
      <div class="legend">
        <span><i class="legend-swatch" style="background:var(--bar-red)"></i>Before</span>
        <span><i class="legend-swatch" style="background:var(--bar-blue)"></i>After</span>
      </div>
      <svg class="chart" width="240" height="90" viewBox="0 0 240 90" aria-label="Bar chart of results">
        <line x1="10" y1="84" x2="230" y2="84" stroke="#bbb" stroke-width="1"/>
        <rect x="40" y="44" width="12" height="40" fill="var(--bar-red)"/>
        <rect x="54" y="34" width="12" height="50" fill="var(--bar-blue)"/>
        <rect x="110" y="30" width="12" height="54" fill="var(--bar-red)"/>
        <rect x="124" y="50" width="12" height="34" fill="var(--bar-blue)"/>
        <rect x="180" y="14" width="12" height="70" fill="var(--bar-red)"/>
        <rect x="194" y="24" width="12" height="60" fill="var(--bar-blue)"/>
      </svg>
      <p class="body-copy">Participants saw brighter, more even skin tone after eight weeks of daily use.</p>
      <p class="source-note">Source: internal study, 2019, page 12</p>
      <svg class="chart" width="240" height="70" viewBox="0 0 240 70" aria-label="Comparison bar chart">
        <line x1="60" y1="64" x2="180" y2="64" stroke="#bbb" stroke-width="1"/>
        <rect x="90" y="30" width="26" height="34" fill="var(--bar-blue)"/>
        <rect x="118" y="18" width="26" height="46" fill="var(--bar-orange)"/>
      </svg>
      <p class="body-copy">Skin clarity improved in most users within twelve weeks, with no reported irritation.</p>
      <p class="source-note">Journal of Skin Wellness, 2018, vol. 4</p>
    </article>
  </section>

</body>
</html>
```